Book Cover for Christian Book titled, "Climbing Past the Silver Hills"

Size of book cover will be 6" x 9".
The book is about how a person can know beyond a shadow of a doubt that they will go to heaven when they die.
The Title is "Climbing Past the Silver Hills"
Subtitle is "Finding Lasting Peace Through Daily Quiet Prayer and Reflection."
The front of the book should have title, subtitle, and author. The back of the book and spine should have no text and be a solid color.
The uploaded pic is a possibility for a design; but I'm open to other designs.
Whatever images are used need to be very high quality to meet Marrowind Folio Services guidelines. Also, the finished product needs to be sized to match the MFS guide for a 6x9 book.

```html
<!DOCTYPE html>
<html lang="en">
<head>
<meta charset="utf-8">
<title>Climbing Past the Silver Hills — Cover Wrap</title>
<link rel="stylesheet" href="https://fonts.googleapis.com/css2?family=Libre+Baskerville:wght@400;700&display=swap">
<style>
  :root {
    --page-bg: #e6e6e6;
    --back-cover: #000000;
    --spine: #000000;
    --panel-edge: #3a3a3a;
    --title-ink: #0b0b0b;
    --title-glow: #fff200;
    --subtitle-ink: #ffffff;
    --author-ink: #f4e9d0;
    --sky-top: #4a4257;
    --sky-cloud: #3a2a26;
    --sun-core: #fff6c8;
    --sun-warm: #f7a21b;
    --horizon: #c4560f;
    --sea-mid: #5a1a08;
    --sea-deep: #1c0603;
  }
  * { margin: 0; padding: 0; box-sizing: border-box; }
  html, body {
    width: 1200px;
    height: 803px;
    overflow: hidden;
    background: var(--page-bg);
  }
  .cover-wrap {
    position: absolute;
    top: 72px;
    left: 142px;
    display: flex;
  }
  .cover {
    position: relative;
    width: 440px;
    height: 660px;
    overflow: hidden;
  }
  .cover--back { background: var(--back-cover); }
  .cover-spine {
    width: 36px;
    height: 660px;
    background: var(--spine);
    border-left: 1px solid var(--panel-edge);
    border-right: 1px solid var(--panel-edge);
  }
  .cover__artwork {
    position: absolute;
    inset: 0;
    background:
      radial-gradient(ellipse 38% 16% at 50% 50%, var(--sun-core) 0%, rgba(255,220,120,0.85) 35%, rgba(247,162,27,0) 100%),
      radial-gradient(ellipse 90% 40% at 50% 50%, rgba(247,162,27,0.9) 0%, rgba(196,86,15,0.4) 55%, rgba(196,86,15,0) 100%),
      linear-gradient(to bottom,
        var(--sky-top) 0%,
        var(--sky-cloud) 14%,
        #8a4a2a 28%,
        var(--sun-warm) 46%,
        var(--horizon) 56%,
        var(--sea-mid) 66%,
        var(--sea-deep) 100%);
  }
  .cover__title {
    position: absolute;
    top: 74px;
    left: 0;
    right: 0;
    text-align: center;
    font-family: "Libre Baskerville", Georgia, serif;
    font-weight: 700;
    font-size: 50px;
    line-height: 1.08;
    color: var(--title-ink);
    text-shadow:
      0 0 3px var(--title-glow),
      0 0 6px var(--title-glow),
      0 0 10px var(--title-glow),
      0 0 14px rgba(255,242,0,0.7);
  }
  .cover__subtitle {
    position: absolute;
    top: 392px;
    left: 40px;
    right: 40px;
    text-align: center;
    font-family: "Libre Baskerville", Georgia, serif;
    font-weight: 700;
    font-size: 15px;
    line-height: 1.35;
    color: var(--subtitle-ink);
  }
  .cover__author {
    position: absolute;
    bottom: 44px;
    left: 0;
    right: 0;
    text-align: center;
    font-family: "Libre Baskerville", Georgia, serif;
    font-weight: 700;
    font-size: 20px;
    letter-spacing: 0.08em;
    color: var(--author-ink);
  }
</style>
</head>
<body>
  <main class="cover-wrap">
    <section class="cover cover--back" aria-label="Back cover, solid colour"></section>
    <div class="cover-spine" aria-label="Spine, solid colour"></div>
    <section class="cover cover--front">
      <div class="cover__artwork" role="img" aria-label="Photograph of a golden sunset breaking through dark clouds over a calm sea"></div>
      <h1 class="cover__title">Climbing<br>Past the<br>Silver<br>Hills</h1>
      <p class="cover__subtitle">Finding Lasting Peace Through Daily Quiet Prayer and Reflection.</p>
      <p class="cover__author">Daniel Ashford</p>
    </section>
  </main>
</body>
</html>
```